Brenlow Development and Management Corp Stationery Design Project

Based on the logo, a stationary format that can be used for correspondence with all project stakeholders. Typically this involves landowners, public officials, general public, and investors. It needs to be clean and professional, representing the two engineers that manage the company.
Updates

Reason: Logo design finalized. Project updated for revisitation. Thanks,

Target Market(s)

Public officials, investors, project stakeholders, and landowners. All or english speaking, residing in North America. Company is based in Calgary, Alberta, Canada. Project values range fro $10MM to $500MM CAD.

Industry/Entity Type

It Company

Requirements
Should not have
• No references to tropics, palm trees, or similar beaches.

```html
<!DOCTYPE html>
<html lang="en">
<head>
<meta charset="utf-8">
<title>Brenlow Development and Management Corp – Stationery</title>
<link rel="stylesheet" href="https://fonts.googleapis.com/css2?family=Arimo:wght@400;700&family=Cinzel:wght@700&display=swap">
<style>
  :root {
    --backdrop: #ebebeb;
    --paper: #f8f8f8;
    --brand-green: #a3c12c;
    --ink-grey: #6b6b6b;
    --rule-grey: #8a8a8a;
    --soft-grey: #9b9b9b;
    --deco-grey: #e8e8e8;
  }
  * { box-sizing: border-box; margin: 0; padding: 0; }
  html, body { width: 1200px; height: 815px; overflow: hidden; }
  body {
    position: relative;
    background: var(--backdrop);
    font-family: "Arimo", Arial, sans-serif;
    color: var(--ink-grey);
  }
  .sheet {
    position: absolute;
    top: 72px;
    width: 483px;
    height: 681px;
    background: var(--paper);
    border-top: 5px solid var(--brand-green);
    box-shadow: 0 2px 6px rgba(0,0,0,0.12);
    overflow: hidden;
  }
  .sheet--letterhead { left: 80px; }
  .sheet--fax { left: 638px; }

  .corner-decoration {
    position: absolute;
    right: 0;
    bottom: 0;
    width: 160px;
    height: 170px;
    z-index: 0;
    background: linear-gradient(180deg, rgba(232,232,232,0) 0%, var(--deco-grey) 55%, var(--deco-grey) 100%);
  }

  .brand { position: absolute; left: 42px; top: 80px; z-index: 1; }
  .brand__name {
    font-family: "Cinzel", Georgia, serif;
    font-weight: 700;
    font-size: 21px;
    letter-spacing: 0.5px;
    color: var(--brand-green);
    line-height: 1;
  }
  .brand__tagline {
    margin-top: 4px;
    font-size: 6.5px;
    color: var(--soft-grey);
  }

  .fax-title {
    position: absolute;
    right: 38px;
    top: 50px;
    font-size: 62px;
    font-weight: 400;
    line-height: 1;
    color: #5f5f5f;
    letter-spacing: 1px;
    z-index: 1;
  }

  .fax-details {
    position: absolute;
    left: 40px;
    top: 135px;
    width: 405px;
    border-collapse: collapse;
    font-size: 7.5px;
    font-weight: 700;
    color: var(--ink-grey);
    z-index: 1;
  }
  .fax-details td {
    border: 1px solid var(--rule-grey);
    height: 14.5px;
    padding: 0 4px;
  }
  .fax-details .label { width: 42px; }
  .fax-details .value { width: 160px; }

  .fax-options {
    position: absolute;
    left: 40px;
    top: 222px;
    width: 405px;
    height: 16px;
    display: grid;
    grid-template-columns: 80px 78px 90px 76px 1fr;
    border: 1px solid var(--rule-grey);
    background: #efefef;
    font-size: 7px;
    font-weight: 700;
    z-index: 1;
  }
  .fax-options__item {
    display: flex;
    align-items: center;
    justify-content: center;
    gap: 3px;
    border-left: 1px solid var(--rule-grey);
  }
  .fax-options__item:first-child { border-left: none; }
  .checkbox {
    width: 5px; height: 5px;
    border: 0.8px solid var(--ink-grey);
    display: inline-block;
  }

  .fax-comments {
    position: absolute;
    left: 40px;
    top: 238px;
    width: 405px;
    height: 371px;
    border: 1px solid var(--rule-grey);
    border-top: none;
    text-align: center;
    font-size: 7.5px;
    padding-top: 14px;
    background: transparent;
    z-index: 1;
  }

  .contact {
    position: absolute;
    left: 40px;
    top: 636px;
    display: flex;
    font-size: 6.5px;
    line-height: 10px;
    color: var(--ink-grey);
    z-index: 1;
  }
  .contact__group { padding-right: 12px; margin-right: 13px; border-right: 1px solid #c8c8c8; }
  .contact__group:last-child { border-right: none; }
  .contact__line { display: flex; align-items: center; gap: 5px; }
  .contact__icon { width: 8px; height: 8px; flex: none; }
</style>
</head>
<body>

<section class="sheet sheet--letterhead" aria-label="Letterhead">
  <div class="corner-decoration" role="img" aria-label="Faint brand decoration in the lower corner"></div>
  <div class="brand">
    <div class="brand__name">BRENLOW</div>
    <div class="brand__tagline">Development and Management Corp</div>
  </div>
  <footer class="contact">
    <div class="contact__group">
      <div class="contact__line"><svg class="contact__icon" viewBox="0 0 8 8"><rect width="8" height="8" rx="1.5" fill="#a3c12c"/><path d="M2.3 1.8l1 1-.5.7c.3.7.8 1.2 1.5 1.5l.7-.5 1 1-.7.8C3.6 6 2 4.4 1.6 2.5z" fill="#fff"/></svg>(04) 5291 7740</div>
      <div class="contact__line"><svg class="contact__icon" viewBox="0 0 8 8"><rect width="8" height="8" rx="1.5" fill="#a3c12c"/><rect x="2" y="3" width="4" height="3" fill="#fff"/><rect x="2.7" y="1.8" width="2.6" height="1.4" fill="#fff"/></svg>(04) 5291 7741</div>
    </div>
    <div class="contact__group">
      <div class="contact__line"><svg class="contact__icon" viewBox="0 0 8 8"><rect width="8" height="8" rx="1.5" fill="#a3c12c"/><path d="M1.8 2.5h4.4v3H1.8z M1.8 2.5L4 4.3 6.2 2.5" fill="none" stroke="#fff" stroke-width=".7"/></svg>hello@brenlow.com</div>
      <div class="contact__line"><svg class="contact__icon" viewBox="0 0 8 8"><rect width="8" height="8" rx="1.5" fill="#a3c12c"/><circle cx="4" cy="4" r="2.2" fill="none" stroke="#fff" stroke-width=".7"/><path d="M1.8 4h4.4" stroke="#fff" stroke-width=".6"/></svg>www.brenlow.com</div>
    </div>
    <div class="contact__group">
      <div>Suite 6, 418 Harrow Lane</div>
      <div>Westbridge NW4 7QT</div>
    </div>
  </footer>
</section>

<section class="sheet sheet--fax" aria-label="Fax cover sheet">
  <div class="corner-decoration" role="img" aria-label="Faint brand decoration in the lower corner"></div>
  <div class="brand">
    <div class="brand__name">BRENLOW</div>
    <div class="brand__tagline">Development and Management Corp</div>
  </div>
  <h1 class="fax-title">FAX</h1>

  <table class="fax-details">
    <tr><td class="label">To:</td><td class="value"></td><td class="label">From:</td><td class="value"></td></tr>
    <tr><td class="label">Fax:</td><td class="value"></td><td class="label">Pages:</td><td class="value"></td></tr>
    <tr><td class="label">Phone:</td><td class="value"></td><td class="label">Date:</td><td class="value"></td></tr>
    <tr><td class="label">Re:</td><td class="value"></td><td class="label">CC:</td><td class="value"></td></tr>
  </table>

  <div class="fax-options">
    <div class="fax-options__item"><span class="checkbox"></span>Urgent</div>
    <div class="fax-options__item"><span class="checkbox"></span>For Review</div>
    <div class="fax-options__item"><span class="checkbox"></span>Please Comment</div>
    <div class="fax-options__item"><span class="checkbox"></span>Please Reply</div>
    <div class="fax-options__item"><span class="checkbox"></span>Please Recycle</div>
  </div>
  <div class="fax-comments">COMMENTS:</div>

  <footer class="contact">
    <div class="contact__group">
      <div class="contact__line"><svg class="contact__icon" viewBox="0 0 8 8"><rect width="8" height="8" rx="1.5" fill="#a3c12c"/><path d="M2.3 1.8l1 1-.5.7c.3.7.8 1.2 1.5 1.5l.7-.5 1 1-.7.8C3.6 6 2 4.4 1.6 2.5z" fill="#fff"/></svg>(04) 5291 7740</div>
      <div class="contact__line"><svg class="contact__icon" viewBox="0 0 8 8"><rect width="8" height="8" rx="1.5" fill="#a3c12c"/><rect x="2" y="3" width="4" height="3" fill="#fff"/><rect x="2.7" y="1.8" width="2.6" height="1.4" fill="#fff"/></svg>(04) 5291 7741</div>
    </div>
    <div class="contact__group">
      <div class="contact__line"><svg class="contact__icon" viewBox="0 0 8 8"><rect width="8" height="8" rx="1.5" fill="#a3c12c"/><path d="M1.8 2.5h4.4v3H1.8z M1.8 2.5L4 4.3 6.2 2.5" fill="none" stroke="#fff" stroke-width=".7"/></svg>hello@brenlow.com</div>
      <div class="contact__line"><svg class="contact__icon" viewBox="0 0 8 8"><rect width="8" height="8" rx="1.5" fill="#a3c12c"/><circle cx="4" cy="4" r="2.2" fill="none" stroke="#fff" stroke-width=".7"/><path d="M1.8 4h4.4" stroke="#fff" stroke-width=".6"/></svg>www.brenlow.com</div>
    </div>
    <div class="contact__group">
      <div>Suite 6, 418 Harrow Lane</div>
      <div>Westbridge NW4 7QT</div>
    </div>
  </footer>
</section>

</body>
</html>
```